Redesign retirement planner website

Provide an original design for a website. The site should introduce the retirement planner, explain the basic offerings of his services, and invite the website visitor to enter their name, phone, and email. Please provide a ready-to-publish redesign that can actually be published via a Wordpress template or other major website builder like SquareSpace or Wix. Some introductory content is attached, but feel free to add additional sections/images/blocks/copywriting and rearrange/delete sections entirely to make your design original and compelling. Feel free to pull copywriting from here but again, do not use this original design, feel free to create an entirely NEW design and layout. lynx-mango-trel (dot) sitefolio (dot) com password: 1234 -- FINAL NOTE: Do not choose a stock photo of a man for the retirement planner. This website needs to work well with no photo of the retirement planner himself. Think of a non-face-focused design to win this competition.

Industry/Entity Type

Retirement planner personal website

Number of Pages Required

1 page

Font styles to use
Sans Serif
Decorative

Requirements
Must have
• Please provide a ready-to-publish redesign that can actually be published via a Wordpress template or other major website builder.

```html
<!DOCTYPE html>
<html lang="en">
<head>
<meta charset="utf-8">
<title>Warren Ashby — Counselor &amp; Retirement Specialist</title>
<link href="https://fonts.googleapis.com/css2?family=Satisfy&family=Dancing+Script:wght@600&family=Montserrat:wght@800&family=Work+Sans:wght@400;500;600&display=block" rel="stylesheet">
<style>
:root{
  --gold:#ffc800;
  --black:#050505;
  --panel:#141414;
  --charcoal:#2f2f2f;
  --charcoal-light:#3a3a3a;
  --line:#1f1f1f;
  --text:#e8e8e8;
  --muted:#cfcfcf;
  --olive:#4f420b;
}
*{box-sizing:border-box;margin:0;padding:0}
html,body{width:1200px;height:4211px;overflow:hidden}
body{background:var(--black);color:var(--text);font-family:"Work Sans",Arial,sans-serif;position:relative}
.script{font-family:"Satisfy","Dancing Script",cursive;color:var(--gold);font-weight:400}
.section{position:absolute;left:0;width:1200px}
.section-title{text-align:center;font-size:50px;line-height:60px}
.textured{background:radial-gradient(ellipse at 30% 30%,var(--charcoal-light),var(--charcoal) 55%,#262626 100%)}

/* hero */
.hero{top:0;height:703px;overflow:hidden;background:#1a1714}
.hero-photo{position:absolute;inset:0;background:
  radial-gradient(ellipse 40% 35% at 50% 72%,rgba(150,120,100,.45),transparent 70%),
  radial-gradient(ellipse 30% 60% at 20% 20%,rgba(190,180,160,.35),transparent 70%),
  radial-gradient(ellipse 25% 30% at 85% 30%,rgba(140,110,160,.35),transparent 70%),
  linear-gradient(160deg,#4a4238 0%,#2a2520 45%,#3a2f26 75%,#151210 100%)}
.hero-photo::after{content:"";position:absolute;inset:0;background:rgba(0,0,0,.38)}
.nav{position:absolute;top:0;left:0;right:0;height:92px;display:flex;align-items:center;padding:0 66px 0 66px}
.brand{font-family:"Satisfy","Dancing Script",cursive;color:var(--gold);font-size:36px}
.nav-links{margin-left:auto;display:flex;align-items:center;gap:30px;list-style:none;font-size:15px;font-weight:500;color:#fff}
.nav-links .dot{width:4px;height:4px;border-radius:50%;background:#bbb}
.nav-links .active{border-bottom:1px solid #fff;padding-bottom:6px;margin-top:7px}
.hero-copy{position:absolute;top:228px;left:0;right:0;text-align:center}
.hero-lead{font-family:"Satisfy","Dancing Script",cursive;color:#fff;font-size:36px;line-height:44px}
.hero-title{font-family:"Montserrat",sans-serif;font-weight:800;color:var(--gold);font-size:64px;line-height:77px;margin-top:12px}
.hero-sub{font-family:"Satisfy","Dancing Script",cursive;color:#fff;font-size:38px;line-height:46px;margin-top:8px}

/* about */
.about{top:703px;height:562px;display:flex}
.about-photo{width:600px;height:562px;background:
  radial-gradient(ellipse 30% 40% at 45% 58%,#2a2c3a,transparent 70%),
  linear-gradient(180deg,#d9c4ad 0%,#c3ad98 30%,#8b8f94 48%,#5f6d74 58%,#4f6a3a 78%,#3a4a26 100%)}
.about-body{width:600px;height:562px;padding:118px 70px 0 70px}
.about-body h2{font-size:50px;line-height:60px}
.about-body p{font-size:15.5px;line-height:24px;color:var(--muted);margin-top:22px;max-width:440px}
.btn{display:inline-block;background:var(--gold);color:#111;font-weight:600;font-size:15px;padding:14px 18px}
.about-body .btn{margin-top:50px}

/* specialties */
.specialties{top:1265px;height:925px}
.specialties .section-title{margin-top:80px}
.spec-grid{position:absolute;left:74px;width:1046px}
.spec-row-top{top:190px;height:302px;display:flex}
.spec-row-bottom{top:492px;height:347px;display:flex;border-top:1px solid var(--line)}
.spec{flex:1;text-align:center}
.spec-row-top .spec{padding:40px 55px 0}
.spec-row-bottom .spec{padding:40px 42px 0}
.spec + .spec{border-left:1px solid var(--line)}
.spec.featured{background:var(--panel)}
.spec-icon{display:block;margin:0 auto}
.spec h3{font-size:21px;font-weight:600;color:#fff;margin-top:28px}
.spec p{font-size:13.5px;line-height:21px;color:var(--muted);margin-top:16px}

/* clients */
.clients{top:2190px;height:652px}
.clients .section-title{margin-top:82px}
.review{position:absolute;top:245px;width:520px;height:242px;background:var(--panel);padding:78px 36px 0}
.review .avatar{position:absolute;top:-53px;left:56px;width:106px;height:106px;border-radius:50%;border:3px solid #fff;background:linear-gradient(180deg,#e6e6e6 0%,#bdbdbd 55%,#4a4a4a 100%)}
.review p{font-size:15.5px;line-height:24px;color:var(--muted)}
.review-foot{display:flex;justify-content:space-between;align-items:center;margin-top:26px}
.review-foot strong{font-size:17px;font-weight:600;color:#fff}
.slider{position:absolute;top:527px;left:554px;display:flex;gap:16px}
.slider span{width:38px;height:38px;border-radius:50%;background:#262626;display:flex;align-items:center;justify-content:center}
.slider .next{background:var(--gold)}

/* offerings */
.offerings{top:2842px;height:628px}
.offerings .section-title{margin-top:68px}
.offer{position:absolute;top:193px;width:337px;height:350px;overflow:hidden}
.offer .cap{position:absolute;left:0;right:0;bottom:0;height:98px;background:rgba(79,66,11,.92);display:flex;align-items:center;justify-content:center;text-align:center;font-size:23px;font-weight:600;line-height:29px;color:#fff}
.offer.text{background:var(--olive);text-align:center;padding:62px 36px 0}
.offer.text h3{font-size:24px;font-weight:600;line-height:29px;color:#fff}
.offer.text p{font-size:14.5px;line-height:24px;color:#ddd;margin-top:20px}
.offer.text .btn-dark{display:inline-block;margin-top:24px;background:#111;color:var(--gold);font-weight:600;font-size:14.5px;padding:13px 19px}

/* contact */
.contact{top:3470px;height:629px}
.contact h2{position:absolute;left:72px;top:80px;font-size:50px;line-height:60px}
.contact .tagline{position:absolute;left:74px;top:166px;font-size:18px;font-weight:600;color:#fff}
.details{position:absolute;left:74px;top:218px;width:488px;list-style:none}
.details li{display:flex;align-items:center;height:78px;border-bottom:1px solid #454545}
.details li:last-child{border-bottom:none}
.details .ic{width:48px;height:48px;border-radius:50%;background:#141414;display:flex;align-items:center;justify-content:center;margin-right:18px;flex:none}
.details small{display:block;font-size:13px;color:var(--muted)}
.details b{display:block;font-size:12.5px;font-weight:600;color:#fff;margin-top:4px}
.form{position:absolute;left:635px;top:222px;width:492px}
.field{height:52px;background:#141414;border:1px solid #3a3a3a;display:flex;align-items:center;padding:0 17px;font-size:15px;color:#ddd;margin-bottom:21px}
.field em{font-style:normal;color:var(--gold);margin-left:6px}
.field-row{display:flex;gap:14px}
.field-row .field{flex:1}
.check{display:flex;align-items:center;gap:14px;font-size:15px;color:#ddd;margin-top:-2px}
.check span{width:20px;height:20px;border:2px solid var(--gold)}
.form .btn{margin-top:26px;padding:13px 17px}

/* footer */
.footer{top:4099px;height:112px;background:var(--black);text-align:center}
.footer p{font-size:13.5px;color:#ddd;margin-top:30px}
.footer ul{list-style:none;display:flex;justify-content:center;align-items:center;gap:14px;margin-top:18px;font-size:13.5px;color:var(--gold)}
.footer ul .dot{width:3px;height:3px;border-radius:50%;background:#999}
</style>
</head>
<body>

<svg width="0" height="0" style="position:absolute">
  <defs><polygon id="star" points="8,0 10.4,5.4 16,6 11.8,9.8 13,15.5 8,12.6 3,15.5 4.2,9.8 0,6 5.6,5.4"/></defs>
</svg>

<header class="section hero">
  <div class="hero-photo" role="img" aria-label="Photograph of an elderly couple holding hands on a bench, shown dimmed"></div>
  <nav class="nav">
    <div class="brand">Warren Ashby</div>
    <ul class="nav-links">
      <li class="active">Home</li><li class="dot"></li>
      <li>Specialities</li><li class="dot"></li>
      <li>Testimonials</li><li class="dot"></li>
      <li>Contact Me</li>
    </ul>
  </nav>
  <div class="hero-copy">
    <div class="hero-lead">I'm a</div>
    <h1 class="hero-title">Counselor &amp;<br>Retirement Specialist</h1>
    <div class="hero-sub">with a unique approach to financial planning</div>
  </div>
</header>

<section class="section about">
  <div class="about-photo" role="img" aria-label="Photograph of a senior couple sitting on a bench by the sea at sunset, seen from behind"></div>
  <div class="about-body textured">
    <h2 class="script">About Me</h2>
    <p>You have a lifetime of accomplishments. Learning about them is my extraordinary honor. When I meet clients to make a plan for their final years of work and savings, I understand my solemn privilege. Your capital is irreplaceable. My job is to maximize its benefit for your health, family, and legacy.</p>
    <a class="btn">Contact Me</a>
  </div>
</section>

<section class="section specialties">
  <h2 class="script section-title">My Specialties</h2>
  <div class="spec-grid spec-row-top">
    <div class="spec">
      <svg class="spec-icon" width="58" height="58" viewBox="0 0 58 58" role="img" aria-label="House icon">
        <path d="M8 26 29 8l21 18" fill="none" stroke="#e86a4a" stroke-width="5" stroke-linejoin="round"/>
        <rect x="15" y="25" width="28" height="20" fill="#fbe3c8"/>
        <circle cx="29" cy="34" r="6" fill="#f6c24a"/>
        <path d="M6 48h46" stroke="#4a90d9" stroke-width="5" stroke-linecap="round"/>
      </svg>
      <h3>Estate Planning</h3>
      <p>Ensure your legacy is protected with comprehensive estate planning. I will guide you through creating wills, trusts, and other essential documents to secure your assets for future generations, ensuring your wishes are honored.</p>
    </div>
    <div class="spec">
      <svg class="spec-icon" width="58" height="58" viewBox="0 0 58 58" role="img" aria-label="Chart icon">
        <rect x="10" y="6" width="40" height="48" rx="3" fill="#e9f2fa"/>
        <rect x="17" y="36" width="6" height="12" fill="#4a90d9"/>
        <rect x="27" y="28" width="6" height="20" fill="#e4575e"/>
        <rect x="37" y="20" width="6" height="28" fill="#f6a540"/>
        <circle cx="14" cy="14" r="8" fill="#5cb87a"/>
      </svg>
      <h3>Retirement Forecasting</h3>
      <p>Plan for a fulfilling retirement with our expert forecasting services. I will analyze your financial situation and future needs to develop a personalized strategy, helping you achieve your retirement goals with confidence.</p>
    </div>
  </div>
  <div class="spec-grid spec-row-bottom">
    <div class="spec">
      <svg class="spec-icon" width="58" height="58" viewBox="0 0 58 58" role="img" aria-label="Document and wallet icon">
        <rect x="10" y="4" width="30" height="40" rx="2" fill="#e9f2fa" stroke="#9cb8d0" stroke-width="2"/>
        <path d="M16 14h18M16 21h18M16 28h12" stroke="#9cb8d0" stroke-width="2.5"/>
        <rect x="26" y="32" width="26" height="18" rx="3" fill="#e49a5a"/>
        <circle cx="44" cy="41" r="3" fill="#fbe3c8"/>
      </svg>
      <h3>Final Expense</h3>
      <p>Prepare for life's final expenses with peace of mind. My services help you plan for costs associated with end-of-life arrangements, alleviating financial stress for your loved ones during a difficult time.</p>
    </div>
    <div class="spec">
      <svg class="spec-icon" width="58" height="58" viewBox="0 0 58 58" role="img" aria-label="Umbrella icon">
        <path d="M6 28a23 23 0 0 1 46 0z" fill="#4a90d9"/>
        <path d="M29 28v18a5 5 0 0 1-10 0" fill="none" stroke="#e49a5a" stroke-width="3.5" stroke-linecap="round"/>
        <circle cx="42" cy="40" r="7" fill="#e4575e"/>
      </svg>
      <h3>Life Insurance</h3>
      <p>Safeguard your family's future with tailored life insurance solutions. I provide expert advice to help you choose the right coverage, ensuring financial security for your loved ones when they need it most.</p>
    </div>
    <div class="spec featured">
      <svg class="spec-icon" width="58" height="58" viewBox="0 0 58 58" role="img" aria-label="Coins with sprout icon">
        <path d="M29 22V10" stroke="#5cb87a" stroke-width="3"/>
        <path d="M29 14c-8 0-12-4-12-8 8 0 12 4 12 8zM29 12c6 0 10-4 10-8-6 0-10 4-10 8z" fill="#7cc46a"/>
        <rect x="14" y="24" width="30" height="8" rx="2" fill="#f6c24a"/>
        <rect x="12" y="33" width="34" height="8" rx="2" fill="#e8a040"/>
        <rect x="14" y="42" width="30" height="8" rx="2" fill="#f6c24a"/>
      </svg>
      <h3>Portfolio Evaluation</h3>
      <p>Maximize your investment potential with our thorough portfolio evaluation. I assess your current assets and provide strategic recommendations to enhance your financial growth and stability.</p>
    </div>
  </div>
</section>

<section class="section clients textured">
  <h2 class="script section-title">My Happy Clients</h2>
  <article class="review" style="left:74px">
    <div class="avatar" role="img" aria-label="Client portrait photo"></div>
    <p>Temporibus autem quibusdam et aut officiis debitis aut rerum necessitatibus saepe eveniet ut et voluptates repudiandae sint et molestiae non recusandae.</p>
    <div class="review-foot"><strong>Margaret Ellis</strong>
      <svg width="100" height="16" viewBox="0 0 100 16" fill="#ffc800"><use href="#star"/><use href="#star" x="21"/><use href="#star" x="42"/><use href="#star" x="63"/><use href="#star" x="84"/></svg>
    </div>
  </article>
  <article class="review" style="left:607px">
    <div class="avatar" role="img" aria-label="Client portrait photo"></div>
    <p>Temporibus autem quibusdam et aut officiis debitis aut rerum necessitatibus saepe eveniet ut et voluptates repudiandae sint et molestiae non recusandae.</p>
    <div class="review-foot"><strong>Harold Brenner</strong>
      <svg width="100" height="16" viewBox="0 0 100 16" fill="#ffc800"><use href="#star"/><use href="#star" x="21"/><use href="#star" x="42"/><use href="#star" x="63"/><use href="#star" x="84"/></svg>
    </div>
  </article>
  <div class="slider">
    <span></span>
    <span class="next"><svg width="12" height="12" viewBox="0 0 12 12"><path d="M4 2l4 4-4 4" stroke="#111" stroke-width="2" fill="none"/></svg></span>
  </div>
</section>

<section class="section offerings">
  <h2 class="script section-title">Insurance Offerings</h2>
  <div class="offer" style="left:74px">
    <div role="img" aria-label="Photograph of a couple silhouetted at sunset, arms forming a heart" style="position:absolute;inset:0;background:radial-gradient(ellipse 40% 30% at 50% 68%,#f2c98a,transparent 70%),linear-gradient(180deg,#8a8f95 0%,#a99a8a 40%,#c9a27a 62%,#3a2d22 100%)"></div>
    <div class="cap">Whole and Universal<br>Life Insurance</div>
  </div>
  <div class="offer text" style="left:432px">
    <h3>Fixed Indexed<br>Annuities</h3>
    <p>Excellent financial vehicles for preserving and protecting capital investments</p>
    <a class="btn-dark">Learn More</a>
  </div>
  <div class="offer" style="left:790px">
    <div role="img" aria-label="Photograph of a red rose, an empty frame and a black ribbon on a dark surface" style="position:absolute;inset:0;background:radial-gradient(ellipse 30% 25% at 22% 18%,#b01c1c,transparent 70%),linear-gradient(135deg,#3a1010 0%,#2a2a2a 40%,#1a1a1a 100%)"></div>
    <div class="cap">Term and Final<br>Expense</div>
  </div>
</section>

<section class="section contact textured">
  <h2 class="script">Contact Me</h2>
  <div class="tagline">Let's plan for golden memories</div>
  <ul class="details">
    <li><span class="ic"><svg width="18" height="14" viewBox="0 0 18 14" fill="none" stroke="#ffc800" stroke-width="1.4"><rect x="1" y="1" width="16" height="12" rx="1"/><path d="M1 2l8 6 8-6"/></svg></span><div><small>Email</small><b>washby@ashbyplan.com</b></div></li>
    <li><span class="ic"><svg width="18" height="18" viewBox="0 0 24 24" fill="none" stroke="#ffc800" stroke-width="1.6"><path d="M5 3h4l2 5-2.5 1.5a11 11 0 0 0 6 6L16 13l5 2v4a2 2 0 0 1-2 2A16 16 0 0 1 3 5a2 2 0 0 1 2-2z"/></svg></span><div><small>Phone</small><b>(555) 214 - 0387</b></div></li>
    <li><span class="ic"><svg width="14" height="14"><circle cx="7" cy="7" r="6" fill="#ffc800"/></svg></span><div><small>ProLink</small><b>https://www.prolink.example/in/warrenashby</b></div></li>
    <li><span class="ic"><svg width="14" height="14"><rect x="1" y="1" width="12" height="12" fill="#ffc800"/></svg></span><div><small>Chatter</small><b>https://www.chatter.example/@warren.ashby</b></div></li>
  </ul>
  <form class="form">
    <div class="field-row">
      <div class="field">First Name<em>*</em></div>
      <div class="field">Last Name<em>*</em></div>
    </div>
    <div class="field">Email<em>*</em></div>
    <div class="field">Phone</div>
    <label class="check"><span></span>Sign up for news and updates</label>
    <a class="btn">Say Hi!</a>
  </form>
</section>

<footer class="section footer">
  <p>© 2024 Warren Ashby. All rights reserved.</p>
  <ul>
    <li>Home</li><li class="dot"></li>
    <li>Specialities</li><li class="dot"></li>
    <li>Testimonials</li><li class="dot"></li>
    <li>Contact Me</li>
  </ul>
</footer>

</body>
</html>
```